Website rebuild, use most content from current site

Hello! I am looking to rebuild my current page as its current its hosted and managed elsewhere..i want to rebuild and upload it to my brightnestweb host so i can manage it in future. happy use use most of my content my website from www.tallowcreeklending.com.au. the site must be easy for my to edit in the future.

I don't want the News, Rates or calculator page.....i would like my chatterbox feeds and Chatterbox review to upload to my page if possible...

These are approximately the pages i want...

Home Page (i want all the lenders logos on this page)
Services (Home Loans, Equipment Finance, Vehicle Finance)
About Us
Lets get started (web form)
Contact Us
Privacy
Terms and conditions

must be mobile compatible and more of a lead generation site prompting clients to contact us....with a modern clean feel..

here are my corporate colour
Blue
PMS coated 2192c
PMS uncoated 2995u
CMYK C80: M10: Y0: K0
RGB R0: G163: B224
HEX #00A3E0

Grey/Black
PMS coated 7540C
PMS uncoated Cool grey 11U
CMYK C0: M0: Y0: K77
RGB R95: G96: B98
HEX #5F6062

Target Market(s)

finance clients

Industry/Entity Type

Finance

Coding

Coded - Design and coding required

Number of Pages Required

5+ page

Font styles to use
Sans Serif

Requirements
Must have
• must be mobile compatible and more of a lead generation site prompting clients to contact us....with a modern clean feel..
• PAGES
• Home Page (i want all the lenders logos on this page)
• Services (Home Loans, Equipment Finance, Vehicle Finance)
• About Us
• Lets get started (web form)
• Contact Us
• Privacy
• Terms and conditions
• here are my corporate colour
• Blue
• PMS coated 2192c
• PMS uncoated 2995u
• CMYK C80: M10: Y0: K0
• RGB R0: G163: B224
• HEX #00A3E0
• Grey/Black
• PMS coated 7540C
• PMS uncoated Cool grey 11U
• CMYK C0: M0: Y0: K77
• RGB R95: G96: B98
• HEX #5F6062
Nice to have
• Chatterbox feeds & testimonials
Should not have
• I don't want the News, Rates or calculator page from my current website

```html
<!DOCTYPE html>
<html lang="en">
<head>
<meta charset="utf-8">
<title>Tallow Creek Lending</title>
<link href="https://fonts.googleapis.com/css2?family=Poppins:wght@300;400;500;600&family=Open+Sans:wght@400;600;700&display=swap" rel="stylesheet">
<style>
:root{
  --blue:#00A3E0;
  --grey:#5F6062;
  --ink:#333436;
  --muted:#8a8b8d;
  --pale:#f3f4f6;
  --line:#e4e5e7;
  --footer:#3b3c3e;
  --white:#ffffff;
}
*{box-sizing:border-box;margin:0;padding:0}
html,body{width:1200px;height:3030px;overflow:hidden}
body{font-family:"Open Sans",Arial,sans-serif;color:var(--grey);background:var(--white);position:relative}
.heading{font-family:"Poppins",Arial,sans-serif;font-weight:400;color:var(--ink);letter-spacing:1px}
.section-title{text-align:center;font-size:27px}
.section-sub{text-align:center;font-size:12px;color:var(--muted);margin-top:10px}

/* header */
.site-header{height:108px;position:relative;background:var(--white)}
.brand{position:absolute;left:84px;top:30px;display:flex;align-items:center;gap:10px}
.brand-mark{width:26px;height:26px;background:var(--blue)}
.brand-name{font-family:"Poppins",Arial,sans-serif;font-weight:500;font-size:20px;color:var(--blue)}
.call{position:absolute;right:84px;top:10px;display:flex;align-items:center;gap:12px;color:var(--blue);font-family:"Poppins",Arial,sans-serif;font-weight:500;font-size:17px}
.call-icon{width:44px;height:44px;border-radius:50%;background:var(--blue);display:flex;align-items:center;justify-content:center}
.main-nav{position:absolute;right:84px;top:70px;display:flex;gap:38px;font-family:"Poppins",Arial,sans-serif;font-size:12px;color:var(--ink)}
.main-nav .active{color:var(--blue)}

/* hero */
.hero{height:524px;position:relative;text-align:center;color:var(--white)}
.hero-photo{position:absolute;inset:0;background:linear-gradient(120deg,#6f6a63 0%,#8c8478 35%,#a59d92 60%,#5e5a55 100%)}
.hero-shade{position:absolute;inset:0;background:rgba(20,22,26,.45)}
.hero-content{position:relative;padding-top:176px}
.hero-title{font-family:"Poppins",Arial,sans-serif;font-weight:300;font-size:40px;color:var(--blue)}
.hero-text{font-size:13px;line-height:26px;width:640px;margin:14px auto 0}
.btn{display:inline-block;background:var(--blue);color:var(--white);font-family:"Poppins",Arial,sans-serif;font-size:15px;padding:11px 30px;letter-spacing:.5px}
.hero .btn{margin-top:28px}
.dots{display:flex;justify-content:center;gap:6px}
.hero .dots{position:absolute;bottom:16px;left:0;right:0}
.dot{width:14px;height:14px;border-radius:50%;border:2px solid var(--white)}
.dot.on{background:var(--blue);border-color:var(--blue)}

/* services */
.services{height:376px;padding-top:38px}
.service-row{display:flex;justify-content:center;gap:60px;margin-top:42px}
.service{width:300px;text-align:center}
.service svg{height:96px}
.service h3{font-family:"Poppins",Arial,sans-serif;font-weight:400;font-size:14px;color:var(--ink);margin-top:12px;letter-spacing:.5px}
.service p{font-size:12px;line-height:24px;color:var(--grey);margin-top:8px;padding:0 26px}

/* features */
.features{height:372px;display:flex;background:var(--pale)}
.features-photo{width:528px;height:372px;background:linear-gradient(135deg,#e8e6e2 0%,#cfd6dd 45%,#b9c4cf 70%,#efeeea 100%)}
.features-copy{padding:34px 0 0 40px;width:600px}
.features-copy h2{font-size:24px}
.features-copy p{font-size:11.5px;line-height:26px;color:var(--muted);margin-top:14px}
.tick-list{list-style:none;margin-top:14px}
.tick-list li{display:flex;align-items:center;gap:20px;font-size:11px;color:var(--muted);letter-spacing:.5px;height:33px}

/* how it works */
.how{height:414px;background:var(--blue);color:var(--white);padding-top:42px;text-align:center}
.how .section-title{color:var(--white)}
.how .section-sub{color:var(--white)}
.steps{position:relative;display:flex;justify-content:center;gap:84px;margin-top:30px}
.step{width:260px}
.step-circle{width:114px;height:114px;border-radius:50%;background:var(--white);margin:0 auto;display:flex;align-items:center;justify-content:center}
.step h3{font-family:"Poppins",Arial,sans-serif;font-weight:500;font-size:17px;margin-top:24px}
.step p{font-size:12px;line-height:24px;margin-top:10px}
.step-arrow{position:absolute;top:24px}

/* testimonials */
.social{height:456px;background:var(--pale);display:flex;padding:36px 0 0 84px;gap:40px}
.feed{width:504px;height:378px;background:var(--white);border:1px solid var(--line)}
.feed-head{height:50px;background:var(--blue);display:flex;align-items:center;padding-left:16px;gap:10px;color:var(--white);font-family:"Open Sans",Arial,sans-serif;font-weight:700;font-size:22px}
.feed-head-box{width:26px;height:26px;background:var(--white)}
.post{display:flex;gap:14px;padding:14px 16px 0 18px;height:148px;border-bottom:1px solid var(--line)}
.avatar{width:62px;height:62px;background:linear-gradient(160deg,#c9b7a6,#8e7b6a)}
.post-body{flex:1;font-size:12px}
.post-meta{color:var(--muted);display:flex;justify-content:space-between}
.post-text{font-style:italic;color:var(--grey);line-height:22px;margin-top:6px}
.post-actions{display:flex;gap:24px;color:var(--muted);font-size:11px;margin-top:12px}
.comment-bar{height:40px;display:flex;align-items:center;padding:0 16px;font-size:11px;color:var(--muted);background:#fafafa;justify-content:space-between}
.testimonials{width:480px}
.testimonials h2{font-size:26px}
.quote{position:relative;padding-left:26px;margin-top:30px;font-size:11.5px;line-height:26px;color:var(--muted)}
.quote p+p{margin-top:12px}
.qmark{position:absolute;font-family:Georgia,serif;font-size:34px;color:var(--ink);line-height:1}
.qmark-end{position:static;font-size:26px;vertical-align:-10px}
.author{margin:16px 0 0 26px;font-family:"Poppins",Arial,sans-serif;color:var(--blue);font-size:15px}
.posted{margin-left:26px;font-size:12px;color:var(--ink)}

/* clients */
.clients{height:468px;padding-top:40px}
.client-grid{display:grid;grid-template-columns:repeat(5,200px);grid-auto-rows:126px;gap:6px;justify-content:center;margin-top:44px}
.client{display:flex;align-items:center;justify-content:center;gap:8px;box-shadow:0 0 0 1px #f0f0f0;font-family:"Open Sans",Arial,sans-serif;font-weight:700;font-size:17px;color:var(--grey);text-align:center}
.client-dot{width:12px;height:12px;background:var(--blue)}
.clients .dots{margin-top:30px}
.clients .dot{width:11px;height:11px;border:none;background:var(--grey)}
.clients .dot.on{background:var(--blue)}

/* footer */
.site-footer{height:312px;background:var(--footer);color:var(--white);position:relative}
.footer-brand{position:absolute;left:100px;top:92px;display:flex;align-items:center;gap:10px}
.footer-brand .brand-name{font-size:19px}
.footer-col{position:absolute;top:30px;font-size:12px;line-height:20px}
.footer-col h4{font-family:"Poppins",Arial,sans-serif;font-weight:500;font-size:15px;letter-spacing:1px;margin-bottom:18px}
.quick{left:350px;width:270px}
.field-row{display:flex;gap:8px}
.field{border:1px solid #bfc0c2;height:34px;font-size:11px;padding:8px 6px;flex:1}
.field.message{height:62px;margin-top:8px}
.quick .btn{font-size:12px;padding:5px 20px;margin-top:14px}
.address{left:656px;width:230px}
.address-line{display:flex;align-items:center;gap:12px;margin-top:10px}
.follow{left:906px;width:200px}
.social-row{display:flex;gap:6px;margin-top:14px}
.social-circle{width:34px;height:34px;border-radius:50%;border:2px solid var(--white)}
.footer-bottom{position:absolute;left:340px;right:84px;top:244px;border-top:1px solid #555658;padding-top:24px;font-size:12px}
.footer-bottom span{text-decoration:underline}
</style>
</head>
<body>

<header class="site-header">
  <div class="brand"><div class="brand-mark"></div><div class="brand-name">Tallow Creek Lending</div></div>
  <div class="call">
    <div class="call-icon">
      <svg width="20" height="20" viewBox="0 0 24 24"><path fill="#fff" d="M6.6 10.8a15.1 15.1 0 0 0 6.6 6.6l2.2-2.2c.3-.3.7-.4 1-.2 1.1.4 2.3.6 3.6.6.6 0 1 .4 1 1V20c0 .6-.4 1-1 1A17 17 0 0 1 3 4c0-.6.4-1 1-1h3.5c.6 0 1 .4 1 1 0 1.3.2 2.5.6 3.6.1.3 0 .7-.2 1z"/></svg>
    </div>
    CALL US : 02 6120 4471
  </div>
  <nav class="main-nav">
    <span class="active">HOME</span><span>SERVICES</span><span>ABOUT US</span><span>LETS GET STARTED</span><span>CONTACT US</span>
  </nav>
</header>

<section class="hero">
  <div class="hero-photo" role="img" aria-label="Photo of a hand with a pen reviewing financial charts and paperwork"></div>
  <div class="hero-shade"></div>
  <div class="hero-content">
    <h1 class="hero-title">Tallow Creek Lending</h1>
    <p class="hero-text">If you're looking for a truly local person who actually owns and operates a local business that is not a part of a franchise organisation and who will take the time to understands you and your personal needs.</p>
    <span class="btn">GET STARTED</span>
  </div>
  <div class="dots"><span class="dot"></span><span class="dot on"></span><span class="dot"></span></div>
</section>

<section class="services">
  <h2 class="heading section-title">OUR SERVICES</h2>
  <p class="section-sub">No matter your financial situation, we've got the service (and solution) to help you!</p>
  <div class="service-row">
    <div class="service">
      <svg viewBox="0 0 100 96" width="100">
        <path d="M14 44 50 12l36 32" fill="none" stroke="#00A3E0" stroke-width="6" stroke-linejoin="round"/>
        <path d="M24 38v26M76 38v26" stroke="#00A3E0" stroke-width="6"/>
        <text x="50" y="60" text-anchor="middle" font-family="Poppins,Arial,sans-serif" font-size="30" font-weight="600" fill="#333436">$</text>
        <path d="M8 72h22l16 6h22l-4 8H30l-22-2z" fill="#333436"/>
      </svg>
      <h3>HOME LOANS</h3>
      <p>We'll find a Home Loan that's right for Recent research has found that broker</p>
    </div>
    <div class="service">
      <svg viewBox="0 0 100 96" width="100">
        <rect x="18" y="66" width="10" height="24" fill="#333436"/>
        <rect x="34" y="56" width="10" height="34" fill="#333436"/>
        <rect x="50" y="46" width="10" height="44" fill="#333436"/>
        <rect x="66" y="36" width="10" height="54" fill="#333436"/>
        <path d="M18 58 44 44l14 6 26-26" fill="none" stroke="#00A3E0" stroke-width="5"/>
        <path d="M74 20h14v14z" fill="#00A3E0"/>
        <text x="36" y="34" text-anchor="middle" font-family="Poppins,Arial,sans-serif" font-size="30" font-weight="600" fill="#333436">$</text>
      </svg>
      <h3>EQUIPMENT FINANCE</h3>
      <p>Starting a new business, looking to expand or modernise your existing business.</p>
    </div>
    <div class="service">
      <svg viewBox="0 0 100 96" width="100">
        <path d="M14 62 22 44h40l8 18v20H14z" fill="#333436"/>
        <rect x="26" y="48" width="32" height="10" fill="#fff"/>
        <circle cx="26" cy="70" r="5" fill="#fff"/><circle cx="58" cy="70" r="5" fill="#fff"/>
        <rect x="14" y="82" width="10" height="8" fill="#333436"/><rect x="60" y="82" width="10" height="8" fill="#333436"/>
        <circle cx="72" cy="30" r="18" fill="#00A3E0"/>
        <text x="72" y="38" text-anchor="middle" font-family="Poppins,Arial,sans-serif" font-size="22" font-weight="600" fill="#fff">£</text>
      </svg>
      <h3>VEHICLE FINANCE</h3>
      <p>Found a car on drivelist? buying privately from a friend, or a dealership? Can we help</p>
    </div>
  </div>
</section>

<section class="features">
  <div class="features-photo" role="img" aria-label="Photo of an adviser reviewing paperwork with a couple at a table"></div>
  <div class="features-copy">
    <h2 class="heading">OUR FEATURES</h2>
    <p>If you're looking for a truly local person who actually owns and operates a local business that is not part of a franchise or other large organisation and who will take the time to understands you &amp; your personal needs, you can't go wrong with Daniel at Tallow Creek Lending.</p>
    <ul class="tick-list">
      <li><svg width="12" height="10" viewBox="0 0 12 10"><path d="M1 5l3.5 3.5L11 1" fill="none" stroke="#00A3E0" stroke-width="2.4"/></svg>PRODUCT KNOWLEDGE</li>
      <li><svg width="12" height="10" viewBox="0 0 12 10"><path d="M1 5l3.5 3.5L11 1" fill="none" stroke="#00A3E0" stroke-width="2.4"/></svg>SAVE TIME</li>
      <li><svg width="12" height="10" viewBox="0 0 12 10"><path d="M1 5l3.5 3.5L11 1" fill="none" stroke="#00A3E0" stroke-width="2.4"/></svg>CONVENIENCE</li>
      <li><svg width="12" height="10" viewBox="0 0 12 10"><path d="M1 5l3.5 3.5L11 1" fill="none" stroke="#00A3E0" stroke-width="2.4"/></svg>IT'S FREE</li>
      <li><svg width="12" height="10" viewBox="0 0 12 10"><path d="M1 5l3.5 3.5L11 1" fill="none" stroke="#00A3E0" stroke-width="2.4"/></svg>DID YOU KNOW</li>
    </ul>
  </div>
</section>

<section class="how">
  <h2 class="heading section-title">HOW IT WORKS</h2>
  <p class="section-sub">No matter your financial situation, we've got the service (and solution) to help you!</p>
  <div class="steps">
    <div class="step">
      <div class="step-circle">
        <svg width="56" height="56" viewBox="0 0 56 56" fill="none" stroke="#00A3E0" stroke-width="3">
          <circle cx="16" cy="12" r="6"/><path d="M6 28c0-6 4-9 10-9s10 3 10 9"/>
          <circle cx="40" cy="32" r="6"/><path d="M30 48c0-6 4-9 10-9s10 3 10 9"/>
          <path d="M32 8h18M32 14h12M6 38h16M6 44h12"/>
        </svg>
      </div>
      <h3>STEP 01</h3>
      <p>Contact us to arrange a free, no-obligation appointment where we can discuss your needs and financial situation.</p>
    </div>
    <div class="step">
      <div class="step-circle">
        <svg width="60" height="56" viewBox="0 0 60 56" fill="none" stroke="#00A3E0" stroke-width="3">
          <path d="M12 4h22l8 8v12"/><path d="M12 4v20"/><path d="M18 14h12M18 20h16"/>
          <path d="M4 24h20l4 5h28v23H4z" fill="#00A3E0"/>
        </svg>
      </div>
      <h3>STEP 02</h3>
      <p>We will sift through thousands of home loan products across more than 30 lenders, and make recommendations based on your needs.</p>
    </div>
    <div class="step">
      <div class="step-circle">
        <svg width="60" height="56" viewBox="0 0 60 56" fill="none" stroke="#00A3E0" stroke-width="3">
          <rect x="6" y="6" width="48" height="34" rx="2"/>
          <path d="M20 22l7 7 14-14" stroke-width="4"/>
          <path d="M30 40v8M18 50h24"/>
        </svg>
      </div>
      <h3>STEP 03</h3>
      <p>Once you're happy, you can submit your home loan application 100% online through this website!</p>
    </div>
    <svg class="step-arrow" style="left:370px" width="90" height="50" viewBox="0 0 90 50"><path d="M4 46C16 16 44 6 78 10" fill="none" stroke="#fff" stroke-width="2" stroke-dasharray="4 4"/><path d="M74 4l10 6-10 6" fill="none" stroke="#fff" stroke-width="2"/></svg>
    <svg class="step-arrow" style="left:728px" width="90" height="50" viewBox="0 0 90 50"><path d="M4 6C18 36 46 44 78 40" fill="none" stroke="#fff" stroke-width="2" stroke-dasharray="4 4"/><path d="M74 34l10 6-10 6" fill="none" stroke="#fff" stroke-width="2"/></svg>
  </div>
</section>

<section class="social">
  <div class="feed">
    <div class="feed-head"><span class="feed-head-box"></span>chatterbox</div>
    <div class="post">
      <div class="avatar" role="img" aria-label="Profile photo of the commenter"></div>
      <div class="post-body">
        <div class="post-meta"><span>16hrs</span><span>• ⌄</span></div>
        <p class="post-text">Sed ut perspiciatis unde omnis iste natus error sit voluptatem accu doloremque laudantium, totam rem aperiam, eaque</p>
        <div class="post-actions"><span>Like</span><span>|</span><span>Comments</span><span>|</span><span>Share</span></div>
      </div>
    </div>
    <div class="post">
      <div class="avatar" role="img" aria-label="Profile photo of the commenter"></div>
      <div class="post-body">
        <div class="post-meta"><span>16hrs</span><span>• ⌄</span></div>
        <p class="post-text">Sed ut perspiciatis unde omnis iste natus error sit voluptatem accu doloremque laudantium, totam rem aperiam, eaque</p>
        <div class="post-actions"><span>Like</span><span>|</span><span>Comments</span><span>|</span><span>Share</span></div>
      </div>
    </div>
    <div class="comment-bar"><span>Write a Comment......</span><span>▢ ○</span></div>
  </div>
  <div class="testimonials">
    <h2 class="heading">OUR TESTIMONIALS</h2>
    <div class="quote">
      <span class="qmark" style="left:0;top:-2px">“</span>
      <p>Highly recommend! Daniel's personalised and professional service was fantastic. To have someone local with genuine industry experience made the whole process far easier and more efficient. Thanks again Daniel we will definitely be using you in again in the future.</p>
      <p>To have someone local with genuine industry experience made the whole process far easier and more efficient. Thanks again Daniel we will definitely be using you in again in the future. <span class="qmark qmark-end">”</span></p>
    </div>
    <p class="author">Priya Marsh – Wellbrook</p>
    <p class="posted">posted on 25 Sep 2017</p>
  </div>
</section>

<section class="clients">
  <h2 class="heading section-title">FEATURE CLIENT</h2>
  <p class="section-sub">No matter your financial situation, we've got the service (and solution) to help you!</p>
  <div class="client-grid">
    <div class="client"><span class="client-dot"></span>Harbourline Bank</div>
    <div class="client">Kestrel</div>
    <div class="client">Summit Mutual</div>
    <div class="client"><span class="client-dot"></span>Bank of Riverton</div>
    <div class="client">Keyhome Loans</div>
    <div class="client">Westgate Bank</div>
    <div class="client">Coastal Bank</div>
    <div class="client">Federal Commons</div>
    <div class="client">Larch Financial</div>
    <div class="client">Orbit Direct</div>
  </div>
  <div class="dots"><span class="dot"></span><span class="dot on"></span><span class="dot"></span></div>
</section>

<footer class="site-footer">
  <div class="footer-brand"><div class="brand-mark"></div><div class="brand-name">Tallow Creek Lending</div></div>
  <div class="footer-col quick">
    <h4>QUICK CONTACT</h4>
    <div class="field-row"><div class="field">Name :</div><div class="field">Phone :</div></div>
    <div class="field message">Message :</div>
    <span class="btn">SUBMIT</span>
  </div>
  <div class="footer-col address">
    <h4>OUR ADDRESS</h4>
    <p>Tallow Creek Lending<br>Representative 118204 of Keystone Broker Group Pty Ltd ACN 412 557 903,</p>
    <div class="address-line"><svg width="12" height="12" viewBox="0 0 24 24"><path fill="#fff" d="M6.6 10.8a15.1 15.1 0 0 0 6.6 6.6l2.2-2.2c.3-.3.7-.4 1-.2 1.1.4 2.3.6 3.6.6.6 0 1 .4 1 1V20c0 .6-.4 1-1 1A17 17 0 0 1 3 4c0-.6.4-1 1-1h3.5c.6 0 1 .4 1 1 0 1.3.2 2.5.6 3.6.1.3 0 .7-.2 1z"/></svg>Phone : 02 6120 4471</div>
    <div class="address-line"><svg width="13" height="11" viewBox="0 0 13 11"><rect x=".75" y=".75" width="11.5" height="9.5" fill="none" stroke="#fff" stroke-width="1.5"/><path d="M1 1l5.5 5L12 1" fill="none" stroke="#fff" stroke-width="1.5"/></svg>daniel@tallowcreeklending.com.au</div>
  </div>
  <div class="footer-col follow">
    <h4>FOLLOW US</h4>
    <p>Lorem ipsum dolor sit amet, conse ctetur adipiscing elit. Nulla in purus nibh. Donec ornare</p>
    <div class="social-row"><span class="social-circle"></span><span class="social-circle"></span><span class="social-circle"></span><span class="social-circle"></span><span class="social-circle"></span></div>
  </div>
  <div class="footer-bottom">© Copy right 2017 &nbsp;Tallow Creek Lending.All rights reserved <span>Privacy</span> &nbsp;| &nbsp;<span>Terms &amp; conditions</span></div>
</footer>

</body>
</html>
```